Weight loss surgery restaurant card

We need to create a card for patients who have undergone weight loss surgery to take to restaurants so they can request smaller meals. These patients have had surgery on their stomach so that they can only consume half to one cup of food at a time. So normal sized restaurant meals are way too big (and cost a lot). This card they can present to the restaurant to communicate the fact that they have had weight loss surgery and therefore request a smaller meal portion at reduced cost

Target Market(s)

Restaurants serving weight loss surgery patients

Industry/Entity Type

Health Care

Contact Information for Business Card

This will be a plastic card similar to business card size.

Requirements
Must have
• The front of the card should include the following text:
• The individual bearing this card has undergone weight loss surgery.
• This surgery restricts portion sizes to between half and one cup of food at a time.
• Please give consideration to allowing smaller portions of your regular meals to be ordered to reduce wastage and excess costs.
• Example: a half size portion priced at two thirds of usual cost.
• The back of the card will have spaces for the person to write certain information. These are the categories that can be filled in by hand:
• Name:
• Procedure performed:
• Date of procedure (month/year):
• Treating Clinic Name:
• Treating Clinic Signature:
• Somewhere down the bottom should be something along the lines of:
• supplied from bernardwhitlow.com.au
Nice to have
• A nice design with imagery/colours etc ... not just the text on a white background! Bright attractive colours preferred.
• I have uploaded my logo ... a roughly triangular image followed by my name etc. The triangular logo image could be used somewhere on the card and this logo can be interchangeable for other clinics who purchase the card.
• **Please note that I don't want my name to be included as part of the logo on the card ... just use the triangular image on the side of the logo without the following name**
• Also, the colouring of the card does not have to reflect my logo colours as I am anticipating interchanging this logo with other logos if other clinics choose to adopt the card. I am interested to see other, more generic, colour choices as well as my logo colours

```html
<!DOCTYPE html>
<html lang="en">
<head>
<meta charset="utf-8">
<title>Weight Loss Surgery Restaurant Card</title>
<link href="https://fonts.googleapis.com/css2?family=Open+Sans:ital,wght@0,700;1,700&display=swap" rel="stylesheet">
<style>
  :root {
    --ink-blue: #2e4d9b;
    --band-red: #df4016;
    --band-orange: #f5a85a;
    --rule-orange: #f3a65c;
    --star-red: #e0401a;
    --teal: #1f9c90;
    --paper: #ffffff;
  }
  html, body {
    margin: 0;
    padding: 0;
    width: 1000px;
    height: 1200px;
    overflow: hidden;
    background: var(--paper);
    font-family: "Open Sans", Arial, sans-serif;
  }
  .canvas { position: relative; width: 1000px; height: 1200px; }
  .card {
    position: absolute;
    box-sizing: border-box;
    border: 2px solid var(--ink-blue);
    background: var(--paper);
    overflow: hidden;
  }
  .card-front { left: 165px; top: 125px; width: 666px; height: 429px; }
  .card-back  { left: 165px; top: 635px; width: 668px; height: 429px; }
  .card-bands { position: absolute; inset: 0; width: 100%; height: 100%; }

  .notice {
    position: absolute;
    left: 83px;
    margin: 0;
    color: var(--ink-blue);
    font-style: italic;
    font-weight: 700;
    font-size: 15.5px;
    line-height: 23px;
    letter-spacing: -0.1px;
  }
  .notice-lead { font-family: Arial, "Open Sans", sans-serif; font-size: 16.5px; }
  .star {
    position: absolute;
    left: 51px;
    width: 17px;
    height: 17px;
  }
  .divider {
    position: absolute;
    left: 90px;
    width: 273px;
    height: 2px;
    background: linear-gradient(90deg, rgba(243,166,92,0) 0%, var(--rule-orange) 25%, var(--rule-orange) 75%, rgba(243,166,92,0) 100%);
  }

  .supplier-note {
    position: absolute;
    left: 39px;
    top: 214px;
    transform: translate(-50%, -50%) rotate(-90deg);
    white-space: nowrap;
    color: var(--paper);
    font-style: italic;
    font-weight: 700;
    font-size: 15px;
  }
  .clinic-mark {
    position: absolute;
    right: 30px;
    top: 40px;
    display: flex;
    align-items: center;
    gap: 6px;
  }
  .clinic-mark-dot { width: 14px; height: 14px; border-radius: 50%; background: var(--teal); }
  .clinic-mark-name { color: var(--ink-blue); font-weight: 700; font-size: 13px; }

  .entry-fields { position: absolute; left: 203px; top: 133px; width: 420px; margin: 0; padding: 0; list-style: none; }
  .entry-field {
    display: flex;
    align-items: center;
    height: 36px;
    color: var(--ink-blue);
    font-style: italic;
    font-weight: 700;
    font-size: 15px;
    white-space: nowrap;
  }
  .entry-line {
    flex: 1;
    margin-left: 8px;
    height: 0;
    border-top: 1.5px dashed var(--rule-orange);
    border-image: repeating-linear-gradient(90deg, var(--rule-orange) 0 10px, transparent 10px 22px) 1;
  }
</style>
</head>
<body>
<div class="canvas">

  <section class="card card-front" aria-label="Card front">
    <svg class="card-bands" viewBox="0 0 666 429" preserveAspectRatio="none" aria-hidden="true">
      <path d="M313,0 Q487,214 313,429 L666,429 L666,0 Z" fill="var(--band-orange)"/>
      <path d="M335,0 Q535,214 335,429 L666,429 L666,0 Z" fill="var(--band-red)"/>
      <path d="M365,0 Q549,214 365,429 L666,429 L666,0 Z" fill="var(--ink-blue)"/>
    </svg>

    <svg class="star" style="top:68px" viewBox="0 0 20 20" aria-hidden="true"><polygon points="10,1 12.6,7.2 19.2,7.6 14.1,11.8 15.8,18.3 10,14.7 4.2,18.3 5.9,11.8 0.8,7.6 7.4,7.2" fill="var(--star-red)"/></svg>
    <p class="notice notice-lead" style="top:62px">&nbsp;The individual bearing this card<br>has undergone weight loss surgery.</p>
    <div class="divider" style="top:119px"></div>

    <svg class="star" style="top:135px" viewBox="0 0 20 20" aria-hidden="true"><polygon points="10,1 12.6,7.2 19.2,7.6 14.1,11.8 15.8,18.3 10,14.7 4.2,18.3 5.9,11.8 0.8,7.6 7.4,7.2" fill="var(--star-red)"/></svg>
    <p class="notice" style="top:132px">&nbsp;This surgery restricts portion sizes to<br>between half and one cup of food at a time.</p>
    <div class="divider" style="top:189px"></div>

    <svg class="star" style="top:204px" viewBox="0 0 20 20" aria-hidden="true"><polygon points="10,1 12.6,7.2 19.2,7.6 14.1,11.8 15.8,18.3 10,14.7 4.2,18.3 5.9,11.8 0.8,7.6 7.4,7.2" fill="var(--star-red)"/></svg>
    <p class="notice" style="top:201px">&nbsp;Please give consideration to allowing<br>&nbsp;smaller portions of your regular meals<br>&nbsp;to be ordered to reduce wastage and<br>excess costs.</p>
    <div class="divider" style="top:304px"></div>

    <svg class="star" style="top:325px" viewBox="0 0 20 20" aria-hidden="true"><polygon points="10,1 12.6,7.2 19.2,7.6 14.1,11.8 15.8,18.3 10,14.7 4.2,18.3 5.9,11.8 0.8,7.6 7.4,7.2" fill="var(--star-red)"/></svg>
    <p class="notice" style="top:316px">&nbsp;Example: a half size portion priced<br>at two thirds of usual cost.</p>
  </section>

  <section class="card card-back" aria-label="Card back">
    <svg class="card-bands" viewBox="0 0 668 429" preserveAspectRatio="none" aria-hidden="true">
      <rect x="0" y="0" width="668" height="429" fill="var(--ink-blue)"/>
      <path d="M112,0 Q44,214 112,429 L668,429 L668,0 Z" fill="var(--band-red)"/>
      <path d="M160,0 Q86,214 160,429 L668,429 L668,0 Z" fill="var(--band-orange)"/>
      <path d="M215,0 Q115,214 215,429 L668,429 L668,0 Z" fill="var(--paper)"/>
    </svg>

    <p class="supplier-note">supplied from bernardwhitlow.com.au</p>

    <div class="clinic-mark">
      <span class="clinic-mark-dot"></span>
      <span class="clinic-mark-name">Harbourline Clinic</span>
    </div>

    <ul class="entry-fields">
      <li class="entry-field">Name:<span class="entry-line"></span></li>
      <li class="entry-field">Procedure performed:<span class="entry-line"></span></li>
      <li class="entry-field">Date of procedure (month/year):<span class="entry-line"></span></li>
      <li class="entry-field">Treating Clinic Name:<span class="entry-line"></span></li>
      <li class="entry-field">Treating Clinic Signature<span class="entry-line"></span></li>
    </ul>
  </section>

</div>
</body>
</html>
```